Coming Soon page for a new fitness startup

We are a new startup based in Toronto, Canada working on a site and mobile app where people can register for athletic events such as running, cycling, triathlon, SUP, etc.

Participants will also be able to manage their clubs and team, and connect their fitness trackers so they have all their fitness data and friends in one place.

I like very simple designs and lots of whitespace. So no need for icons or unnecessary graphics.

I prefer having a mobile phone app instead of a hero image. No need to worry about the details within the mobile app for now, we can fill it in later. Here are some landing pages that I like.
https://pixelshelf.example/tormundlaksa/buckets/493817-Landing-Page

Attached is a wireframe that gives some sample content for each of the sections. Please do not take the wireframe too literally, it is only meant to illustrate the content that we are experimenting with and should give an idea of how much text will be on the page.

I have also attached the company logo files. The logo is not being used yet so feel free to simplify the logo if it doesn't look great with your design. For example, I'm ok with just the name "vexqari" in white if that looks better.

Target Market(s)

Ages 25 to 45. Interested in running, cycling, triathlon, SUP, etc.

Industry/Entity Type

Fitness

Coding

Coded - Design and coding required

Number of Pages Required

1 page

Requirements
Should not have
• Any photos should not contain track and field events, or people in a gym. Any photos should have people running or cycling outdoors. I know that photos can be easily swapped out but it is distracting to review a design that has the wrong photos.

```html
<!DOCTYPE html>
<html lang="en">
<head>
<meta charset="utf-8">
<title>vexqari — Coming Soon</title>
<link href="https://fonts.googleapis.com/css2?family=Montserrat:wght@600;700&family=Mulish:wght@400;600;700;800&display=swap" rel="stylesheet">
<style>
  :root {
    --red: #d41f32;
    --ink: #2b2b2b;
    --body: #444444;
    --muted: #9a9a9a;
    --frame: #e6e6e6;
    --hero-bg: #f1f1f1;
    --section-bg: #f3f3f3;
    --field-bg: #f1f1f1;
    --white: #ffffff;
    --phone-panel: #8a8a8a;
    --star: #f2c21b;
  }
  * { box-sizing: border-box; margin: 0; padding: 0; }
  html, body { width: 790px; height: 1200px; overflow: hidden; background: var(--frame); }
  body { font-family: 'Mulish', Arial, sans-serif; color: var(--body); }
  .canvas { position: relative; width: 790px; height: 1200px; }
  .page { position: absolute; left: 9px; top: 9px; width: 772px; height: 1182px; background: var(--white); overflow: hidden; }
  .abs { position: absolute; }

  .hero-bg { left: 0; top: 0; width: 772px; height: 460px; }
  .launch-banner { right: 0; top: 0; width: 319px; height: 79px; }
  .launch-text { right: 40px; top: 33px; color: var(--white); font-family: 'Montserrat', sans-serif; font-weight: 700; font-size: 12px; letter-spacing: 0.2px; }
  .brand { left: 21px; top: 24px; font-family: 'Mulish', sans-serif; font-weight: 700; font-size: 31px; color: var(--red); letter-spacing: 0.3px; }

  /* phone */
  .phone { left: 44px; top: 113px; width: 173px; height: 340px; border: 3px solid #3a3a3a; border-radius: 22px; background: var(--white); box-shadow: 0 6px 10px rgba(0,0,0,0.12); overflow: hidden; }
  .phone-notch { left: 40px; top: -3px; width: 87px; height: 12px; background: #1f1f1f; border-radius: 0 0 9px 9px; }
  .phone-brand { left: 0; width: 167px; top: 22px; text-align: center; font-weight: 700; font-size: 20px; color: var(--red); }
  .phone-photo { left: 11px; top: 65px; width: 148px; height: 98px; background: linear-gradient(160deg, #b9b3a6 0%, #8f8c84 55%, #6f6d68 100%); }
  .phone-panel { left: 11px; top: 163px; width: 148px; height: 110px; background: var(--phone-panel); }
  .phone-avatar { left: 61px; top: 142px; width: 48px; height: 48px; border-radius: 50%; background: #4a4a4a; border: 3px solid var(--white); }
  .phone-name { left: 11px; width: 148px; top: 198px; text-align: center; color: var(--white); font-style: italic; font-weight: 700; font-size: 8px; }
  .phone-loc { left: 11px; width: 148px; top: 210px; text-align: center; color: var(--white); font-style: italic; font-size: 6px; }
  .phone-stars { left: 11px; width: 148px; top: 224px; text-align: center; color: var(--star); font-size: 10px; letter-spacing: 0.5px; }
  .phone-events { left: 35px; top: 243px; width: 96px; height: 18px; border: 1.5px solid var(--white); border-radius: 9px; color: var(--white); font-size: 7px; font-weight: 700; display: flex; justify-content: space-between; align-items: center; padding: 0 10px; }
  .phone-nav { left: 0; top: 276px; width: 167px; height: 56px; display: flex; }
  .nav-item { flex: 1; display: flex; flex-direction: column; align-items: center; padding-top: 8px; border-right: 1px solid #e3e3e3; font-size: 4.6px; color: #777; text-align: center; line-height: 1.3; }
  .nav-item:last-child { border-right: none; }
  .nav-item svg { width: 14px; height: 14px; margin-bottom: 4px; }

  /* hero copy */
  .hero-kicker { left: 270px; top: 130px; font-family: 'Montserrat', sans-serif; font-weight: 700; font-size: 18.5px; color: var(--ink); letter-spacing: -0.2px; }
  .hero-title { left: 269px; top: 148px; font-family: 'Montserrat', sans-serif; font-weight: 700; font-size: 35px; color: var(--ink); letter-spacing: -0.3px; }
  .hero-copy { left: 270px; top: 199px; width: 470px; font-size: 10.2px; line-height: 15.2px; color: var(--body); }
  .signup-title { left: 280px; width: 444px; top: 298px; text-align: center; font-weight: 700; font-size: 16px; color: var(--ink); }
  .signup-sub { left: 280px; width: 444px; top: 326px; text-align: center; font-weight: 700; font-size: 13px; color: var(--muted); }
  .email-input { left: 292px; top: 353px; width: 304px; height: 33px; border: 1.5px solid #d7d7d7; border-radius: 10px; background: var(--white); font-size: 10.5px; font-weight: 600; color: var(--ink); padding-left: 16px; line-height: 30px; }
  .notify-btn { left: 602px; top: 353px; width: 109px; height: 33px; background: var(--red); border-radius: 10px; color: var(--white); font-family: 'Montserrat', sans-serif; font-weight: 600; font-size: 10.5px; letter-spacing: 0.6px; text-align: center; line-height: 33px; box-shadow: 0 2px 3px rgba(0,0,0,0.15); }

  /* features */
  .section-title { left: 0; width: 772px; top: 516px; text-align: center; font-weight: 700; font-size: 16.5px; color: var(--ink); }
  .section-sub { left: 0; width: 772px; top: 544px; text-align: center; font-weight: 700; font-size: 13px; color: var(--muted); }
  .feature { top: 600px; width: 205px; }
  .feature h3 { font-weight: 700; font-size: 12.5px; color: var(--red); margin-bottom: 6px; }
  .feature p { font-size: 10.2px; line-height: 15.2px; color: var(--body); }

  /* organizer band */
  .band-bg { left: 0; top: 744px; width: 772px; height: 404px; }
  .org-title { left: 42px; top: 844px; font-weight: 700; font-size: 17px; color: var(--ink); }
  .org-copy { left: 42px; top: 884px; width: 380px; font-weight: 700; font-size: 10.2px; line-height: 15.2px; color: var(--ink); }
  .org-copy p { margin-bottom: 14.5px; }

  .contact-card { left: 483px; top: 835px; width: 243px; height: 244px; background: var(--white); }
  .contact-head { left: 0; top: 0; width: 243px; height: 34px; background: var(--red); color: var(--white); font-family: 'Montserrat', sans-serif; font-weight: 700; font-size: 12px; text-align: center; line-height: 34px; box-shadow: 0 3px 4px rgba(0,0,0,0.18); }
  .field-label { left: 19px; font-size: 8px; font-weight: 700; color: var(--ink); }
  .field-label span { color: var(--red); }
  .field { left: 18px; width: 206px; background: var(--field-bg); }
  .submit-btn { left: 18px; top: 207px; width: 89px; height: 21px; background: #2f2f2f; color: var(--white); font-family: 'Montserrat', sans-serif; font-weight: 600; font-size: 9.5px; text-align: center; line-height: 21px; }

  /* footer */
  .footer { left: 0; top: 1139px; width: 772px; height: 43px; background: var(--white); }
  .footer-links { left: 13px; top: 15px; font-size: 8px; font-weight: 800; color: var(--ink); }
  .footer-links .sep { margin: 0 6px; }
  .footer-social { left: 361px; top: 11px; display: flex; gap: 2px; }
  .footer-social span { width: 15px; height: 15px; border: 1.2px solid var(--ink); border-radius: 50%; display: block; }
  .footer-copy { right: 13px; top: 15px; font-size: 8px; font-weight: 800; color: var(--ink); }
</style>
</head>
<body>
<div class="canvas">
  <main class="page">

    <svg class="abs hero-bg" viewBox="0 0 772 460" aria-hidden="true">
      <polygon points="0,0 772,0 772,415 390,443 300,452 0,450" fill="#f3f3f3"/>
      <polygon points="180,0 420,0 300,200" fill="#f7f7f7"/>
      <polygon points="560,80 772,40 772,300" fill="#ececec"/>
      <polygon points="400,300 772,250 772,415 560,430" fill="#e9e9e9"/>
      <polygon points="0,200 140,120 120,330 0,380" fill="#f7f7f7"/>
      <polygon points="620,380 772,330 772,415" fill="#e3e3e3"/>
    </svg>

    <svg class="abs launch-banner" viewBox="0 0 319 79" aria-hidden="true">
      <polygon points="0,0 319,0 319,79 78,79" fill="var(--red)"/>
    </svg>
    <div class="abs launch-text">LAUNCHING IN SPRING 2018</div>

    <div class="abs brand">vexqari</div>

    <div class="abs phone">
      <div class="abs phone-notch"></div>
      <div class="abs phone-brand">vexqari</div>
      <div class="abs phone-photo" role="img" aria-label="Photo of runners racing on an outdoor road"></div>
      <div class="abs phone-panel"></div>
      <div class="abs phone-avatar" role="img" aria-label="Member profile photo"></div>
      <div class="abs phone-name">Darren Holt</div>
      <div class="abs phone-loc">Halifax, Nova Scotia</div>
      <div class="abs phone-stars">★★★★★</div>
      <div class="abs phone-events"><span>EVENTS</span><span>&gt;10</span></div>
      <div class="abs phone-nav">
        <div class="nav-item">
          <svg viewBox="0 0 14 14"><circle cx="7" cy="7" r="6" fill="none" stroke="#555" stroke-width="1"/><circle cx="7" cy="5.5" r="2" fill="none" stroke="#555" stroke-width="1"/><path d="M3.5 11 Q7 7.5 10.5 11" fill="none" stroke="#555" stroke-width="1"/></svg>
          ACCOUNT
        </div>
        <div class="nav-item">
          <svg viewBox="0 0 14 14"><circle cx="9" cy="2.5" r="1.5" fill="#555"/><path d="M3 6 L6 4.5 L9 5 L7 9 L10 12 M7 9 L4 11 L1.5 10.5 M9 5 L11 7.5 L13 7" fill="none" stroke="#555" stroke-width="1.4" stroke-linecap="round"/></svg>
          ATHLETIC<br>EVENTS
        </div>
        <div class="nav-item">
          <svg viewBox="0 0 14 14"><circle cx="4" cy="4" r="1.6" fill="#555"/><circle cx="10" cy="4" r="1.6" fill="#555"/><circle cx="7" cy="5" r="1.8" fill="#555"/><rect x="2.5" y="6.5" width="3" height="6" rx="1" fill="#555"/><rect x="8.5" y="6.5" width="3" height="6" rx="1" fill="#555"/><rect x="5.2" y="7.5" width="3.6" height="6" rx="1" fill="#555"/></svg>
          MANAGE<br>TEAM
        </div>
        <div class="nav-item">
          <svg viewBox="0 0 14 14"><rect x="2.5" y="2" width="9" height="11" fill="none" stroke="#555" stroke-width="1"/><rect x="5" y="1" width="4" height="2" fill="#555"/><path d="M4 8 L6 8 L7 6 L8 10 L9 8 L10 8" fill="none" stroke="#555" stroke-width="0.9"/></svg>
          FITNESS<br>TRACKERS
        </div>
        <div class="nav-item">
          <svg viewBox="0 0 14 14"><rect x="1.5" y="2.5" width="11" height="10" fill="none" stroke="#555" stroke-width="1"/><line x1="1.5" y1="5" x2="12.5" y2="5" stroke="#555" stroke-width="1"/><g fill="#555"><rect x="3.5" y="6.5" width="1.5" height="1.5"/><rect x="6.2" y="6.5" width="1.5" height="1.5"/><rect x="9" y="6.5" width="1.5" height="1.5"/><rect x="3.5" y="9.3" width="1.5" height="1.5"/><rect x="6.2" y="9.3" width="1.5" height="1.5"/><rect x="9" y="9.3" width="1.5" height="1.5"/></g></svg>
          ORGANIZING<br>EVENTS
        </div>
      </div>
    </div>

    <h2 class="abs hero-kicker">CONNECT YOUR TRAINING, FRIENDS AND EVENTS</h2>
    <h1 class="abs hero-title">IN ONE PLACE</h1>
    <p class="abs hero-copy">Lorem ipsum dolor sit amet, consectetuer adipiscing elit, sed diam nonummy nibh euismod tincid unt ut laoreet dolore magna aliquam erat volutpat. Ut wisi enim ad minim veniam, quis nostrud exerci tation ullamcorper suscipit lobortis nisl ut aliquip ex ea commodo consequat. Duis autem vel eum iriure dolor in hendrerit in vulputate velit esse molestie consequat.</p>

    <h3 class="abs signup-title">Join our email list</h3>
    <p class="abs signup-sub">A referral program is coming and you'll want to be the first to know</p>
    <div class="abs email-input">Email Address</div>
    <div class="abs notify-btn">NOTIFY ME</div>

    <h2 class="abs section-title">Training and Racing all in one place</h2>
    <p class="abs section-sub">A new fitness community is coming soon</p>

    <div class="abs feature" style="left:47px">
      <h3>Sign up for events</h3>
      <p>Lorem ipsum dolor sit amet, consectetue adipiscing elit, sed diam nonummy nibh euismod tincidunt ut laoreet dolore mag aliquam erat volutpat.</p>
    </div>
    <div class="abs feature" style="left:290px">
      <h3>Invite your friends</h3>
      <p>Lorem ipsum dolor sit amet, consectetue adipiscing elit, sed diam nonummy nibh euismod tincidunt ut laoreet dolore mag aliquam erat volutpat.</p>
    </div>
    <div class="abs feature" style="left:533px">
      <h3>Connect your workouts</h3>
      <p>Lorem ipsum dolor sit amet, consectetue adipiscing elit, sed diam nonummy nibh euismod tincidunt ut laoreet dolore mag aliquam erat volutpat.</p>
    </div>

    <svg class="abs band-bg" viewBox="0 0 772 404" aria-hidden="true">
      <polygon points="0,0 385,30 772,0 772,404 0,404" fill="var(--section-bg)"/>
    </svg>

    <h2 class="abs org-title">Organizing an event?</h2>
    <div class="abs org-copy">
      <p>Attracting participants is hard work.</p>
      <p>With your event listed on vexqari, we'll not only handle the registration and payment process, we've also made it our own personal mission to drive up participation numbers across all events.An online presence requires effort and planning.</p>
      <p>Contact us to learn more.</p>
    </div>

    <form class="abs contact-card">
      <div class="abs contact-head">WE'D LOVE TO HEAR FROM YOU</div>
      <label class="abs field-label" style="top:46px">Your name<span>*</span></label>
      <div class="abs field" style="top:62px;height:17px"></div>
      <label class="abs field-label" style="top:86px">Email address<span>*</span></label>
      <div class="abs field" style="top:101px;height:17px"></div>
      <label class="abs field-label" style="top:125px">How can we help?</label>
      <div class="abs field" style="top:140px;height:59px"></div>
      <div class="abs submit-btn">SUBMIT</div>
    </form>

    <footer class="abs footer">
      <div class="abs footer-links">About Us<span class="sep">I</span>Developers<span class="sep">I</span>Careers</div>
      <div class="abs footer-social" aria-label="Social links"><span></span><span></span><span></span></div>
      <div class="abs footer-copy">Copyright © 2018 vexqari, Inc.</div>
    </footer>

  </main>
</div>
</body>
</html>
```